Business Card Design

Looking for business card designs for a new business. there will be two cards of the same design (both lots of information below in contact info). We would like the logo diagonally across the card with the information split above and below the logo similar to sketch. happy to look at similar alternatives
Please use same colours as in logo design

Industry/Entity Type

Business

Contact Information for Business Card

Colin Marwood
mob - 0498 172 943
ph - 02 6812 4300
fax - 02 6812 4900
email - col@ridgelinetrusses.com.au
14 Larchmont Road, Westdale NSW 2340

Gavin Holloway
mob - 0421 830 576
ph - 02 6812 4300
fax - 02 6812 4900
email - gavin@ridgelinetrusses.com.au

```html
<!DOCTYPE html>
<html lang="en">
<head>
<meta charset="utf-8">
<title>Ridgeline Frames &amp; Trusses — Business Cards</title>
<link rel="stylesheet" href="https://fonts.googleapis.com/css2?family=Montserrat:wght@700;800&family=Didact+Gothic&display=swap">
<style>
  :root {
    --backdrop: #e6e2db;
    --card-white: #ffffff;
    --card-black: #231f20;
    --band-grey: #949494;
    --teal: #2b8b8a;
    --ink: #1c1c1c;
    --white: #ffffff;
  }
  * { margin: 0; padding: 0; box-sizing: border-box; }
  html, body {
    width: 1068px;
    height: 1200px;
    overflow: hidden;
    background: var(--backdrop);
  }
  .card {
    position: absolute;
    left: 76px;
    width: 912px;
    height: 520px;
    overflow: hidden;
  }
  .card--front { top: 69px; background: var(--card-white); }
  .card--back  { top: 631px; background: var(--card-black); }

  .diagonal-band {
    position: absolute;
    left: 0;
    top: 0;
    width: 912px;
    height: 520px;
  }
  .diagonal-band polygon { fill: var(--band-grey); }

  .name-ribbon {
    position: absolute;
    left: 24px;
    top: 31px;
    width: 354px;
    height: 53px;
    background: var(--teal);
    clip-path: polygon(0 0, 100% 0, 93% 50%, 100% 100%, 0 100%);
    color: var(--white);
    font-family: "Montserrat", sans-serif;
    font-weight: 700;
    font-size: 27px;
    letter-spacing: 1px;
    line-height: 53px;
    padding-left: 24px;
    text-transform: uppercase;
    white-space: nowrap;
  }
  .personal-contact {
    position: absolute;
    left: 44px;
    top: 100px;
    list-style: none;
    font-family: "Didact Gothic", sans-serif;
    color: var(--ink);
  }
  .personal-contact li {
    display: flex;
    align-items: center;
    gap: 8px;
    height: 32px;
    margin-bottom: 11px;
  }
  .personal-contact .mobile { font-size: 23px; }
  .personal-contact .email { font-size: 21px; }
  .icon { width: 16px; height: 16px; flex: none; fill: var(--ink); }

  .wordmark {
    position: absolute;
    display: flex;
    align-items: center;
    gap: 16px;
    font-family: "Montserrat", sans-serif;
    font-weight: 800;
    line-height: 1;
    white-space: nowrap;
  }
  .wordmark__square { flex: none; background: var(--teal); }
  .wordmark__name { display: flex; flex-direction: column; }

  .card--front .wordmark {
    left: 455px;
    top: 270px;
    transform: translate(-50%, -50%) rotate(-33deg);
    color: var(--ink);
  }
  .card--front .wordmark__square { width: 78px; height: 78px; }
  .card--front .wordmark__line1 { font-size: 78px; }
  .card--front .wordmark__line2 { font-size: 40px; margin-top: 2px; }

  .office-contact {
    position: absolute;
    left: 575px;
    top: 405px;
    list-style: none;
    font-family: "Didact Gothic", sans-serif;
    font-size: 19px;
    color: var(--ink);
    transform: rotate(-28deg);
    transform-origin: left top;
    white-space: nowrap;
  }
  .office-contact li {
    display: flex;
    align-items: flex-start;
    gap: 8px;
    margin-bottom: 4px;
    line-height: 1.15;
  }
  .office-contact .icon { margin-top: 2px; }

  .card--back .wordmark {
    left: 450px;
    top: 250px;
    transform: translate(-50%, -50%) rotate(-30deg);
    color: var(--white);
  }
  .card--back .wordmark__square { width: 96px; height: 96px; background: var(--white); }
  .card--back .wordmark__line1 { font-size: 96px; }
  .card--back .wordmark__line2 { font-size: 49px; margin-top: 2px; }
</style>
</head>
<body>

<section class="card card--front" aria-label="Business card front">
  <svg class="diagonal-band" viewBox="0 0 912 520" aria-hidden="true">
    <polygon points="165,520 764,0 912,0 912,76 400,520"/>
  </svg>

  <div class="name-ribbon">Colin Marwood</div>

  <ul class="personal-contact">
    <li class="mobile">
      <svg class="icon" viewBox="0 0 16 16" aria-hidden="true"><rect x="4" y="1" width="8" height="14" rx="1.5"/><rect x="5.5" y="3" width="5" height="8" fill="#fff"/></svg>
      0498 172 943
    </li>
    <li class="email">
      <svg class="icon" viewBox="0 0 16 16" aria-hidden="true"><rect x="1" y="3" width="14" height="10" rx="1"/><path d="M2 4 L8 9 L14 4" fill="none" stroke="#fff" stroke-width="1.4"/></svg>
      col@ridgelinetrusses.com.au
    </li>
  </ul>

  <div class="wordmark">
    <span class="wordmark__square"></span>
    <span class="wordmark__name">
      <span class="wordmark__line1">Ridgeline</span>
      <span class="wordmark__line2">Frames &amp; Trusses</span>
    </span>
  </div>

  <ul class="office-contact">
    <li>
      <svg class="icon" viewBox="0 0 16 16" aria-hidden="true"><path d="M4 1.5 L6.5 4.5 L5 6.5 Q7 9.5 9.5 11 L11.5 9.5 L14.5 12 L12.5 14.5 Q6 13.5 1.5 4 Z"/></svg>
      02 6812 4300
    </li>
    <li>
      <svg class="icon" viewBox="0 0 16 16" aria-hidden="true"><rect x="4" y="1.5" width="8" height="4"/><rect x="1" y="6" width="14" height="6" rx="1"/><rect x="4" y="11" width="8" height="3.5"/></svg>
      02 6812 4900
    </li>
    <li>
      <svg class="icon" viewBox="0 0 16 16" aria-hidden="true"><path d="M8 1 A5 5 0 0 1 13 6 C13 9.5 8 15 8 15 C8 15 3 9.5 3 6 A5 5 0 0 1 8 1 Z"/><circle cx="8" cy="6" r="2" fill="#fff"/></svg>
      <span>14 Larchmont Road<br>Bramleigh NSW 2999</span>
    </li>
  </ul>
</section>

<section class="card card--back" aria-label="Business card back">
  <div class="wordmark">
    <span class="wordmark__square"></span>
    <span class="wordmark__name">
      <span class="wordmark__line1">Ridgeline</span>
      <span class="wordmark__line2">Frames &amp; Trusses</span>
    </span>
  </div>
</section>

</body>
</html>
```